Joomla Responsive Website Template for an International Biotechnology Company

Our client is a biotechnology company that uses silver-based technology to help make products antimicrobial, antibacterial, and anti fungal. We need a Joomla-based template that is responsive/mobile friendly when viewed on tablets or smartphones. We are looking for a template design for the home page and subpages. We are replacing the current website http://www.velmora-labs.com with a new website being built here: http://velmoraclean.com.stagehost.com/velmoraprime/. What we have now on the site is the basic wire frame. This is the desired layout and pictures we want to use. We would like you to add some design elements to make the website more professional looking and polished. Please refer to the attached style guide to help you in choosing the color. The client does like the green leaf, which is included in the last page of style guide and may be good for a background image. While the Velmora logo and leaf are green, we do not want to overuse the color green. The client does own other technologies that we will be promoting on the site and the logos for these technologies are attached below. These logos are Tusk, Velmora-Prime, and Wisp. We will be using this website to promote the technologies, the markets the technologies serve; drinking water, medical devices, apparel and textiles, and architectural surfaces, and to promote the customer using these devices. Please make the design "clean" and not cluttered, as these technologies are used to fight "dirty things".
Updates

Hello Designers! Thank you all very much for your design submissions. They were simply excellent. Due to the Holidays and New Years, many of the client's team members have been on vacation. We expect to have feedback shortly and pick the top design soon there after. Again, thank you all very much and hope the New Year brings you continued success. Best, Dorian

Industry/Entity Type

Biotechnology

Coding

Coded - Design and coding required

```html
<!DOCTYPE html>
<html lang="en">
<head>
<meta charset="utf-8">
<title>Velmora — Antimicrobial Technology</title>
<link href="https://fonts.googleapis.com/css2?family=Ubuntu:wght@400;500&family=Open+Sans:wght@400;600;700&display=swap" rel="stylesheet">
<style>
:root{
  --green:#6cbd45;
  --green-dark:#4f9a2c;
  --ink:#333;
  --text:#555;
  --muted:#777;
  --line:#d8d8d8;
  --red:#e2231a;
  --blue:#1a7ac4;
  --social:#2a8fd0;
}
*{margin:0;padding:0;box-sizing:border-box}
html,body{width:860px;height:1200px;overflow:hidden;background:#fff}
body{position:relative;font-family:"Open Sans",Arial,sans-serif;color:var(--text)}
.abs{position:absolute}
.h{font-family:"Ubuntu","Open Sans",sans-serif;color:var(--ink);font-weight:400}

.brand{left:80px;top:10px;height:36px;display:flex;align-items:center;gap:8px;color:var(--green);font-family:"Ubuntu",sans-serif;font-weight:500;font-size:28px;line-height:36px}
.brand i{display:block;width:14px;height:14px;background:var(--green)}
.search{left:541px;top:16px;width:169px;height:24px;border:1px solid var(--line);font-size:11px;line-height:22px;padding-left:10px;color:#666}
.search svg{position:absolute;right:8px;top:4px}
.social{top:20px;display:flex;align-items:center;gap:4px;font-size:10px;font-weight:600;color:var(--ink);line-height:14px}
.social i{display:block;width:9px;height:9px;background:var(--social)}

.nav{left:0;top:57px;width:860px;height:30px;border-top:1px solid var(--line);border-bottom:1px solid var(--line);background:linear-gradient(#fff,#fafafa)}
.nav a{position:absolute;top:0;font-size:11px;line-height:28px;color:var(--ink);text-decoration:none}
.nav .active{border:1px solid var(--line);border-top:2px solid var(--green);border-bottom:none;background:#fff;padding:0 6px;height:30px;top:-1px}
.dropdown{left:383px;top:87px;width:131px;background:#fff;border:1px solid var(--line);box-shadow:0 2px 4px rgba(0,0,0,.15);padding:4px 0;z-index:2}
.dropdown div{font-size:9.5px;line-height:18px;padding-left:8px;color:#777}
.dropdown .on{background:var(--green);color:#fff}

.stage{left:0;top:87px;width:860px;height:300px;background:linear-gradient(#ececec,#fff)}
.slide{left:78px;top:110px;width:703px;height:269px;background:linear-gradient(#fff 0%,#dfeefa 30%,#4f9ad6 55%,#2a76c0 100%)}
.dots{left:402px;top:362px;display:flex;gap:5px}
.dots i{width:10px;height:10px;border-radius:50%;border:2px solid #fff;background:#999;display:block}
.dots i.on{background:var(--green)}

.center{left:0;width:860px;text-align:center}
.market{width:178px;text-align:center}
.icon{width:52px;height:52px;border:2px solid #bbb;border-radius:4px;margin:0 auto;background:#fff;display:flex;align-items:center;justify-content:center}
.market h3{font-size:15px;margin-top:10px}
.market p{font-size:11px;line-height:14.5px;margin:5px auto 0;width:152px}

.tech-box{top:691px;width:214px;height:65px;border:2px solid #bbb;border-radius:3px;text-align:center;font-family:"Open Sans",sans-serif;font-weight:700;font-size:30px;line-height:61px;letter-spacing:1px}
.tech-copy{top:765px;width:222px;font-size:10.9px;line-height:16.5px}
.tech-copy b{font-weight:600}
.more{font-size:8.5px;color:var(--green-dark);font-style:italic}

.sec-title{font-size:18px;padding-bottom:6px;border-bottom:1px solid var(--line)}
.about{left:78px;top:896px;width:408px;font-size:10.9px;line-height:18.6px}
.news{left:522px;width:252px;font-size:9px;line-height:13.5px;color:var(--ink)}
.news span{display:block;color:var(--muted);font-size:8.5px;line-height:11px}
.client{top:1107px;height:28px;font-size:15px;font-weight:600;line-height:28px;color:#444;display:flex;align-items:center;gap:6px}
.client i{width:10px;height:10px;display:block;background:#888}
.footer{left:78px;top:1163px;width:700px;border-top:2px solid var(--green);font-size:9.5px;color:#555}
</style>
</head>
<body>
<header>
  <div class="abs brand"><i></i>velmora</div>
  <div class="abs search">Search ...
    <svg width="14" height="14" viewBox="0 0 14 14"><circle cx="5.5" cy="5.5" r="4" fill="none" stroke="#888" stroke-width="1.6"/><line x1="8.5" y1="8.5" x2="13" y2="13" stroke="#888" stroke-width="2"/></svg>
  </div>
  <div class="abs social" style="left:722px"><i></i>Kite</div>
  <div class="abs social" style="left:752px"><i></i>Folk</div>
</header>

<nav class="abs nav">
  <a style="left:166px">Home</a>
  <a style="left:232px">About Us</a>
  <a style="left:313px">Markets</a>
  <a class="active" style="left:383px">Technology</a>
  <a style="left:481px">Customer Programs</a>
  <a style="left:614px">News Highlights</a>
  <a style="left:728px">Contact Us</a>
</nav>

<div class="abs stage"></div>
<div class="abs dropdown">
  <div>Dropdown Option 01</div>
  <div>Dropdown Option 02</div>
  <div class="on">Dropdown Option 03</div>
  <div>Dropdown Option 04</div>
</div>
<div class="abs slide" role="img" aria-label="Clear water surface with rising bubbles"></div>
<div class="abs dots"><i></i><i class="on"></i><i></i><i></i></div>

<h2 class="abs center h" style="top:395px;font-size:21px">Our Market or Services Text</h2>
<p class="abs" style="left:80px;top:428px;width:700px;text-align:center;font-size:11px;line-height:17px">Sed ut perspiciatis unde omnis iste natus error sit voluptatem accusantium doloremque laudantium, totam rem aperiam, eaque ipsa quae ab illo inventore veritatis et quasi architecto beatae.</p>

<div class="abs market" style="left:55px;top:479px">
  <div class="icon"><svg width="30" height="30" viewBox="0 0 30 30"><rect x="4" y="8" width="16" height="6" fill="#999"/><rect x="10" y="4" width="4" height="4" fill="#999"/><path d="M20 8h4v8h-4z" fill="#999"/><path d="M22 20c-2 3 0 6 0 6s2-3 0-6z" fill="#999"/></svg></div>
  <h3 class="h">Drinking Water</h3>
  <p>Lorem ipsum dolor sitamet at consec sit tetur adipiscing elit sed dolet amet</p>
</div>
<div class="abs market" style="left:234px;top:479px">
  <div class="icon"><svg width="32" height="30" viewBox="0 0 32 30"><rect x="3" y="4" width="26" height="20" rx="2" fill="none" stroke="#999" stroke-width="2"/><path d="M16 19l-5-5a3 3 0 0 1 5-3 3 3 0 0 1 5 3z" fill="#999"/></svg></div>
  <h3 class="h">Medical Devices</h3>
  <p>Dong ipsum dolor sitamet at consec sit tetur adipiscing elit sed dolet</p>
</div>
<div class="abs market" style="left:413px;top:479px">
  <div class="icon"><svg width="32" height="30" viewBox="0 0 32 30"><path d="M10 5l-7 5 3 5 3-2v13h14V13l3 2 3-5-7-5c-1 3-3 4-6 4s-5-1-6-4z" fill="#999"/></svg></div>
  <h3 class="h">Apparel &amp; Textiles</h3>
  <p>Lorem ipsum dolor sitamet at consec sit tetur adipiscing elit sed dolet</p>
</div>
<div class="abs market" style="left:599px;top:479px">
  <div class="icon"><svg width="32" height="30" viewBox="0 0 32 30"><path d="M6 25L16 5l10 20z" fill="none" stroke="#999" stroke-width="2"/><line x1="4" y1="25" x2="28" y2="25" stroke="#999" stroke-width="2"/></svg></div>
  <h3 class="h">Architectural Surfaces</h3>
  <p>Lorem ipsum dolor sitamet at consec sit tetur adipiscing elit sed dolet</p>
</div>

<div class="abs" style="left:100px;top:632px;width:660px;height:1px;background:linear-gradient(90deg,transparent,var(--line),transparent)"></div>
<h2 class="abs center h" style="top:647px;font-size:19px">Our Technology</h2>

<div class="abs tech-box" style="left:78px;color:#222">PRIME</div>
<div class="abs tech-box" style="left:324px;color:var(--red)">TUSK</div>
<div class="abs tech-box" style="left:565px;color:var(--blue)">WISP</div>

<p class="abs tech-copy" style="left:82px"><b style="color:#222">Velmora Prime</b> is the latest in cutting edge technology available from Corvane. Combining the power of two proprietary technologies <span class="more">... learn more</span></p>
<p class="abs tech-copy" style="left:327px"><b style="color:var(--red)">Corvane Tusk</b> is the latest in cutting edge technology available from Corvane. Combining the power of two proprietary technologies <span class="more">... learn more</span></p>
<p class="abs tech-copy" style="left:569px"><b style="color:var(--blue)">Corvane Wisp</b> is the latest in cutting edge technology available from Corvane. Combining the power of two proprietary technologies <span class="more">... learn more</span></p>

<h2 class="abs h sec-title" style="left:78px;top:855px;width:403px;padding-left:3px">Velmora<sup style="font-size:10px">®</sup> Antimicrobial</h2>
<p class="abs about">Velmora branded antimicrobial technology makes products cleaner and longer lasting with silver, copper and zinc, which have been proven in use throughout history. Velmora antimicrobial technology provides built-in protection by working 24/7 resisting the growth of microbes. We work in close partnership with our customers, from development to end-user marketing, to deliver a product advantage that makes a real difference in the marketplace. *Velmora is an EPA registered ionic silver technology and is not a nanosilver technology.</p>

<h2 class="abs h sec-title" style="left:521px;top:858px;width:253px">News &amp; events</h2>
<div class="abs news" style="top:896px">New Clinical Hygiene Society (CHS) Guidelines Include Velmora Antimicrobial-Treated Catheters<span>Friday, 24 November 2014</span></div>
<div class="abs news" style="top:948px">Riverton Marathon Winner Wears Stridewell Shoes Protected by Velmora Antimicrobial<span>Saturday, 18 November 2014</span></div>
<div class="abs news" style="top:1000px">Velmora Antimicrobial Incorporated into Norvex's Industrial Flooring for Enhanced Microbial Resistance<span>Monday, 10 November 2014</span></div>
<div class="abs" style="left:685px;top:1040px;font-size:8.5px;color:var(--green-dark);text-decoration:underline">More News &amp; Events</div>

<h2 class="abs h sec-title" style="left:78px;top:1063px;width:700px;font-size:18px">Our Clients</h2>
<div class="abs client" style="left:79px"><i></i>Medrix</div>
<div class="abs client" style="left:216px">Aqualine</div>
<div class="abs client" style="left:343px">Purewell</div>
<div class="abs client" style="left:462px">Halvern</div>
<div class="abs client" style="left:557px">Nuvacoat</div>
<div class="abs client" style="left:706px">Tessaro</div>

<footer class="abs footer">
  <div class="abs" style="left:0;top:10px">Copyright © 2014 Velmora. All rights reserved.</div>
  <div class="abs" style="left:233px;top:10px;white-space:nowrap">Home &nbsp;| &nbsp;About Us &nbsp;| &nbsp;Markets &nbsp;| &nbsp;Technology &nbsp;| &nbsp;Customer Programs &nbsp;| &nbsp;News Highlights &nbsp;| &nbsp;Contact Us</div>
</footer>
</body>
</html>
```